"Trade with Tilda" needs a funky and stylish business card

Hi my name is Tilda, I am an experienced Bidnest Prime Vendor with a 100% satisfaction rating and over 400 items sold

My business name and bidnest username is "Trade with Tilda" I sell other peoples items on Bidnest for a commission. The main items I sell are furniture and renovation/building salvage items such as used kitchens, bathrooms , window doors etc.

I will be promoting my service in real estate agent offices, storage facilities, removalists, building and renovating companies.

i believe selling on bidnest is a great way for people to recycle their used goods and salvageable materials and reduce waste and landfill.

Target Market(s)

people selling their homes, renovators, builders, downsizers

Industry/Entity Type

Real Estate

Contact Information for Business Card

Tilda Marlowe
0492716045

Logo Text

Trade with Tilda

Logo styles of interest
Wordmark Logo
Requirements
Must have
• the business card must feature the bidnest logo mentioning primevendorr gold ranked vendor I have attached a copy
Nice to have
• i would like to have the trade with tilda logo written in royal blue

```html
<!DOCTYPE html>
<html lang="en">
<head>
<meta charset="utf-8">
<title>Trade with Tilda — Business Card</title>
<link rel="stylesheet" href="https://fonts.googleapis.com/css2?family=Open+Sans:wght@600&display=swap">
<style>
  :root {
    --stage: #3b63a8;
    --emblem-navy: #16306e;
    --emblem-text: #f2f4f8;
    --ray-orange: #ef8f1f;
    --ray-yellow: #f2d21a;
    --ray-green: #239a52;
    --ray-teal: #1f9a8c;
    --ray-blue: #1f64b4;
    --ray-violet: #7a64b4;
    --ray-magenta: #b2349a;
    --ray-red: #e0245e;
  }

  html, body {
    margin: 0;
    padding: 0;
    width: 1200px;
    height: 900px;
    overflow: hidden;
  }

  body {
    background: var(--stage);
    display: flex;
    align-items: center;
    justify-content: center;
  }

  .business-card {
    position: relative;
    width: 840px;
    height: 480px;
    overflow: hidden;
    border-radius: 4px;
    box-shadow: 0 18px 40px rgba(10, 20, 50, 0.35);
  }

  .sunburst-field {
    position: absolute;
    inset: 0;
    background: linear-gradient(
      125deg,
      var(--ray-orange) 0%,
      var(--ray-red) 16%,
      var(--ray-magenta) 30%,
      var(--ray-violet) 44%,
      var(--ray-blue) 58%,
      var(--ray-teal) 72%,
      var(--ray-green) 84%,
      var(--ray-yellow) 100%
    );
  }

  .brand-emblem {
    position: absolute;
    left: 50%;
    top: 50%;
    width: 250px;
    height: 250px;
    transform: translate(-50%, -50%);
    border-radius: 50%;
    background: var(--emblem-navy);
    display: flex;
    align-items: center;
    justify-content: center;
  }

  .brand-name {
    margin: 0;
    font-family: "Open Sans", sans-serif;
    font-weight: 600;
    font-size: 30px;
    line-height: 1.15;
    color: var(--emblem-text);
    text-align: center;
    letter-spacing: 0.2px;
  }
</style>
</head>
<body>
  <main class="business-card">
    <div class="sunburst-field" role="img" aria-label="Rainbow sunburst of curved swirling rays in orange, red, magenta, violet, blue, green and yellow radiating from the centre"></div>
    <div class="brand-emblem">
      <h1 class="brand-name">Trade with<br>Tilda</h1>
    </div>
  </main>
</body>
</html>
```